Bamboo Toothbrush packaging design

We need a packaging design for a pack of 4 bamboo toothbrushes. The front of the package would need to include the company logo, name of the product - Bamboo Toothbrush, 100% plastic free, and 10% of profit will go to environmental charities . Would like to see some simple or creative graphics to send the message.

Target Market(s)

Retail

Font styles to use
Sans Serif

Colors

Designer to choose colors to be used in the design.

Requirements
Must have
• Just be creative.

```html
<!DOCTYPE html>
<html lang="en">
<head>
<meta charset="utf-8">
<title>Reed Crane Bamboo Toothbrush Carton</title>
<link href="https://fonts.googleapis.com/css2?family=Josefin+Sans:wght@300;400&display=swap" rel="stylesheet">
<style>
  :root {
    --kraft: #c6a88b;
    --kraft-light: #cfb296;
    --ink: #1c3440;
    --dieline: #2a2a2a;
    --paper: #ffffff;
  }
  html, body {
    margin: 0;
    padding: 0;
    width: 1200px;
    height: 2406px;
    overflow: hidden;
    background: var(--paper);
  }
  .carton {
    position: relative;
    width: 1200px;
    height: 2406px;
    font-family: "Josefin Sans", sans-serif;
    color: var(--ink);
  }
  .dieline {
    position: absolute;
    inset: 0;
  }
  .vertical {
    position: absolute;
    writing-mode: vertical-rl;
    white-space: nowrap;
  }
  .brand-name {
    font-size: 78px;
    font-weight: 400;
    line-height: 80px;
    letter-spacing: 1px;
  }
  .brand-front { left: 312px; top: 495px; }
  .brand-back { left: 675px; top: 495px; }
  .product-lines {
    font-size: 38px;
    font-weight: 300;
    line-height: 45px;
    letter-spacing: 0.5px;
  }
  .product-front { left: 312px; top: 1290px; }
  .product-back { left: 680px; top: 1290px; }
  .charity-note {
    left: 552px;
    top: 363px;
    width: 63px;
    height: 729px;
    background: var(--ink);
    color: var(--kraft-light);
    font-size: 27px;
    font-weight: 300;
    letter-spacing: 2.5px;
    line-height: 63px;
    padding-top: 40px;
    box-sizing: border-box;
  }
  .origin-note {
    left: 934px;
    top: 862px;
    font-size: 22px;
    font-weight: 300;
    letter-spacing: 0.8px;
    line-height: 26px;
  }
</style>
</head>
<body>
<main class="carton">
  <svg class="dieline" width="1200" height="2406" viewBox="0 0 1200 2406">
    <defs>
      <linearGradient id="bamboo-tone" x1="0" y1="0" x2="0" y2="1">
        <stop offset="0" stop-color="#1c3440" stop-opacity="0.15"/>
        <stop offset="1" stop-color="#1c3440" stop-opacity="0.55"/>
      </linearGradient>
    </defs>
    <g fill="var(--kraft)" stroke="var(--dieline)" stroke-width="1">
      <polygon class="glue-flap" points="177,398 285,363 285,2025 177,1988"/>
      <polygon class="dust-flap" points="510,273 648,273 655.5,363 510,363"/>
      <path class="tuck-flap" d="M655.5 363 V123 Q655.5 93 685.5 93 H847.5 Q877.5 93 877.5 123 V363 Z"/>
      <rect class="dust-flap" x="877.5" y="273" width="145.5" height="90"/>
      <rect class="carton-body" x="285" y="363" width="738" height="1680"/>
    </g>
    <line x1="655.5" y1="217.5" x2="877.5" y2="217.5" stroke="var(--dieline)" stroke-width="1"/>

    <rect class="bamboo-art" x="410" y="1170" width="168" height="783" fill="url(#bamboo-tone)" role="img" aria-label="Illustration of bamboo stalks with leaves"/>
    <rect class="bamboo-art" x="778" y="1170" width="242" height="783" fill="url(#bamboo-tone)" role="img" aria-label="Illustration of bamboo stalks with leaves"/>

    <g fill="var(--ink)" stroke="var(--dieline)" stroke-width="1">
      <rect class="base-band" x="285" y="1953" width="738" height="90"/>
      <path class="tuck-flap" d="M285 2043 V2287 Q285 2317 315 2317 H480 Q510 2317 510 2287 V2043 Z"/>
      <rect class="dust-flap" x="513" y="2043" width="142.5" height="87"/>
      <rect class="dust-flap" x="877.5" y="2043" width="142.5" height="87"/>
    </g>
    <line x1="285" y1="2187" x2="510" y2="2187" stroke="#0e1d24" stroke-width="1"/>

    <g stroke="var(--dieline)" stroke-width="1">
      <line x1="510" y1="363" x2="510" y2="2043"/>
      <line x1="655.5" y1="363" x2="655.5" y2="2043"/>
      <line x1="877.5" y1="363" x2="877.5" y2="2043"/>
    </g>
  </svg>

  <div class="vertical brand-name brand-front">Reed Crane</div>
  <div class="vertical brand-name brand-back">Reed Crane</div>

  <div class="vertical charity-note">10% of profit will go to environmental charities</div>

  <div class="vertical product-lines product-front">Bamboo Toothbrush<br>100% plastic free</div>
  <div class="vertical product-lines product-back">Bamboo Toothbrush<br>100% plastic free</div>

  <div class="vertical origin-note">Made in China &nbsp;|&nbsp; Distributed by Reed Crane</div>
</main>
</body>
</html>
```